#1 Selling Sweden weight loss supplement comes to USA - LABEL needed!

The number one weight loss in Sweden is coming to USA

-I need a label that is clean and simple but somehow represents, in an abstract way, weight loss or slender.
-The product and water mixed is all the is needed. This too could be represented in the label design.
-The bottle will be white.

-Attached is a picture of a supplement bottle with
--the logo for the company, 'NuKelvara'
--the name of the supplement, 'Kelvara Lithe'
and
--other text that could be included in the final label.

ALSO attached are 2 label designs that I like. This might give you an idea of a direction to go.
Thank You very much.

Target Market(s)

Health conscience people

Industry/Entity Type

Weight

Font styles to use
Sans Serif

Requirements
Must have
• -Size of bottle - 2" wide x 4" high
Nice to have
• *Lowers Hunger up to 50%
• *Decreases cravings or unhealthy foods up to 90%
• *Enhances Weight Loss
• " A Durovix a day keeps hunger away"

```html
<!DOCTYPE html>
<html lang="en">
<head>
<meta charset="utf-8">
<title>Kelvara Lithe – Durovix label</title>
<link rel="stylesheet" href="https://fonts.googleapis.com/css2?family=Roboto:ital,wght@0,300;0,400;1,400&display=swap">
<style>
  :root {
    --paper: #ffffff;
    --navy: #1c1f6b;
    --royal: #2a5fa8;
    --sky: #1e9be0;
    --leaf: #4caf3a;
    --leaf-dark: #2f7d2a;
    --rose: #e0245e;
    --brown: #5a3a22;
  }
  * { margin: 0; padding: 0; box-sizing: border-box; }
  html, body { width: 1200px; height: 786px; overflow: hidden; background: var(--paper); }
  body { position: relative; font-family: "Roboto", Arial, sans-serif; font-weight: 300; }

  .silhouette { position: absolute; left: 0; top: 0; width: 1200px; height: 786px; }
  .silhouette path { fill: none; stroke: var(--sky); stroke-width: 3; stroke-linecap: round; }

  .brand { position: absolute; display: flex; align-items: center; gap: 8px;
           color: var(--navy); font-weight: 300; letter-spacing: -0.5px; white-space: nowrap; }
  .brand-dot { border-radius: 50%; background: var(--leaf); flex: none; }

  .leaf-art { position: absolute; border-radius: 60% 10% 60% 10%;
              background: radial-gradient(ellipse at 40% 40%, var(--leaf), var(--leaf-dark)); }

  .product { position: absolute; color: var(--navy); font-weight: 300; line-height: 1.2; }
  .product .variant { display: block; color: var(--royal); font-size: 0.9em; }
  .product sup { font-size: 0.4em; }

  .tagline { position: absolute; color: var(--rose); font-style: italic; font-weight: 400; line-height: 1.6; }

  .benefits { position: absolute; list-style: none; color: var(--brown); font-weight: 400; }
  .benefits li { display: flex; align-items: flex-start; white-space: nowrap; }
  .tick { flex: none; fill: none; stroke: var(--rose); stroke-width: 2.4; stroke-linecap: round; stroke-linejoin: round; }
</style>
</head>
<body>

<svg class="silhouette" viewBox="0 0 1200 786" aria-hidden="true">
  <!-- large panel -->
  <path d="M108,165 C140,300 150,400 138,480 C125,570 110,640 105,700"/>
  <path d="M392,165 C360,300 352,390 362,470 C375,560 390,640 386,700"/>
  <path d="M252,700 C258,725 262,745 262,758"/>
  <!-- medium panel -->
  <path d="M522,150 C548,300 560,400 552,470 C543,560 518,640 520,745"/>
  <path d="M793,150 C750,320 742,410 758,470 C780,550 800,630 800,745"/>
  <path d="M680,695 C684,720 686,738 686,750"/>
  <!-- narrow panel -->
  <path d="M1003,150 C1038,300 1040,380 1025,480 C1010,580 1005,660 1008,740"/>
</svg>

<section class="label label-large">
  <div class="brand" style="left:148px;top:198px;font-size:44px;">NuKelvara<span class="brand-dot" style="width:15px;height:15px;"></span></div>
  <div class="leaf-art" role="img" aria-label="Two green spinach leaves" style="left:154px;top:314px;width:66px;height:56px;"></div>
  <h1 class="product" style="left:224px;top:304px;font-size:25px;">Kelvara<br>Lithe<span class="variant">Durovix<sup>®</sup></span></h1>
  <p class="tagline" style="left:140px;top:482px;width:250px;text-align:center;font-size:15px;">A Durovix<br>a day keeps hunger away</p>
  <ul class="benefits" style="left:126px;top:585px;width:240px;font-size:11.5px;">
    <li style="margin-bottom:20px;"><svg class="tick" width="22" height="16" viewBox="0 0 22 16"><path d="M3,8 L8,14 L20,2"/></svg><span style="margin-left:6px;">Lowers Hunger up to 50%</span></li>
    <li style="margin-bottom:18px;"><svg class="tick" width="22" height="16" viewBox="0 0 22 16"><path d="M3,8 L8,14 L20,2"/></svg><span style="margin-left:6px;">Decreases cravings or unhealthy foods<br>up to 90%</span></li>
    <li><svg class="tick" width="22" height="16" viewBox="0 0 22 16"><path d="M3,8 L8,14 L20,2"/></svg><span style="margin-left:6px;">Enhances Weight Loss</span></li>
  </ul>
</section>

<section class="label label-medium">
  <div class="brand" style="left:566px;top:186px;font-size:44px;">NuKelvara<span class="brand-dot" style="width:14px;height:14px;"></span></div>
  <div class="leaf-art" role="img" aria-label="Two green spinach leaves" style="left:562px;top:306px;width:74px;height:58px;"></div>
  <h2 class="product" style="left:643px;top:296px;font-size:24px;">Kelvara<br>Lithe<span class="variant">Durovix<sup>®</sup></span></h2>
  <p class="tagline" style="left:545px;top:474px;width:230px;text-align:center;font-size:15px;">A Durovix<br>a day keeps hunger away</p>
  <ul class="benefits" style="left:540px;top:578px;width:240px;font-size:11.5px;">
    <li style="margin-bottom:20px;"><svg class="tick" width="22" height="16" viewBox="0 0 22 16"><path d="M3,8 L8,14 L20,2"/></svg><span style="margin-left:6px;">Lowers Hunger up to 50%</span></li>
    <li style="margin-bottom:18px;"><svg class="tick" width="22" height="16" viewBox="0 0 22 16"><path d="M3,8 L8,14 L20,2"/></svg><span style="margin-left:6px;">Decreases cravings or unhealthy foods<br>up to 90%</span></li>
    <li><svg class="tick" width="22" height="16" viewBox="0 0 22 16"><path d="M3,8 L8,14 L20,2"/></svg><span style="margin-left:6px;">Enhances Weight Loss</span></li>
  </ul>
</section>

<section class="label label-narrow">
  <div class="brand" style="left:1022px;top:192px;font-size:28px;gap:5px;">NuKelvara<span class="brand-dot" style="width:10px;height:10px;"></span></div>
  <div class="leaf-art" role="img" aria-label="Two green spinach leaves" style="left:1034px;top:262px;width:70px;height:60px;"></div>
  <h2 class="product" style="left:1047px;top:332px;font-size:23px;">Kelvara<br>Lithe<span class="variant" style="font-size:17px;">Durovix<sup>®</sup></span></h2>
  <p class="tagline" style="left:1048px;top:510px;width:130px;font-size:15px;">A Durovix<br>a day keeps<br>hunger away</p>
  <ul class="benefits" style="left:1016px;top:614px;width:160px;font-size:9.5px;">
    <li style="margin-bottom:12px;"><svg class="tick" width="16" height="12" viewBox="0 0 22 16"><path d="M3,8 L8,14 L20,2"/></svg><span style="margin-left:4px;">Lowers Hunger up to 50%</span></li>
    <li style="margin-bottom:12px;"><svg class="tick" width="16" height="12" viewBox="0 0 22 16"><path d="M3,8 L8,14 L20,2"/></svg><span style="margin-left:8px;text-align:right;">Decreases cravings or<br>unhealthy foods up to 90%</span></li>
    <li><svg class="tick" width="16" height="12" viewBox="0 0 22 16"><path d="M3,8 L8,14 L20,2"/></svg><span style="margin-left:14px;">Enhances Weight Loss</span></li>
  </ul>
</section>

</body>
</html>
```